Strength and Conditioning Business needs a logo design

We need a logo design for a fitness company based in South Carolina called "K7R Motion Dynamics". We are a group of Strength and Conditioning Coaches that work with youth, high school, collegiate, and professional athletes. We also train general population clients that are looking to improve their overall fitness. Our primary mission is to make sure our athletes are able to gain the greatest benefits from training that will allow them to excel in their sport. We use heavy chains, kettle bells, resistance bands, dumbbells, prowlers (sleds), and multi-functional machines for training. We have a dynamic and collaborative approach that utilizes high-intensity intervals combined with speed, power, agility, and strength training.

Industry/Entity Type

Fitness

Contact Information for Business Card

K7R Motion Dynamics
Lorenzo Baptiste, MA, CPT, NSCP
Head of Athletic Development
Riverbend, ST
Phone: (555) 318-7046
Email: k7rmotiondynamics@quikmailbox.net
Instagram: lift_mentor_lb

Font styles to use
Sans Serif

Colors
9bcb3c
ffffff
000000
474747
ec1f27
7f7f7f
0456a4

Requirements
Must have
• I would like to have a black card with either lime green or bold blue accents along with white and silver. On the back, I would like the name 'K7R Motion Dynamics' with a subheading that says, 'Strength and Conditioning.'
Nice to have
• I really like the designs of the cards I uploaded. For the logo, something clean, bold, and eye-catching would be great.
Should not have
• I do not want a logo that will make it difficult to read.

```html
<!DOCTYPE html>
<html lang="en">
<head>
<meta charset="utf-8">
<title>K7R Motion Dynamics – Business Card</title>
<link rel="stylesheet" href="https://fonts.googleapis.com/css2?family=Russo+One&family=Arimo:wght@400;700&display=swap">
<style>
  :root {
    --lime: #9bcb3c;
    --blue: #2f4fc4;
    --white: #ffffff;
    --black: #0f0f10;
    --card: #18181a;
    --silver: #7f7f7f;
    --emboss: #3c3c3e;
    --backdrop: #3a332f;
  }
  * { margin: 0; padding: 0; box-sizing: border-box; }
  html, body { width: 1200px; height: 900px; overflow: hidden; }
  body {
    background: var(--backdrop);
    font-family: "Arimo", Arial, sans-serif;
    position: relative;
  }
  .card {
    position: absolute;
    left: 280px;
    width: 640px;
    height: 366px;
    background: var(--card);
    border-radius: 4px;
    overflow: hidden;
  }
  .card--back { top: 64px; background: var(--black); }
  .card--front { top: 470px; }

  .brand {
    position: absolute;
    top: 44px;
    left: 48px;
    display: flex;
    align-items: center;
  }
  .brand__mark { width: 150px; height: 150px; flex: none; }
  .brand__divider {
    width: 2px;
    height: 118px;
    margin: 0 22px 0 24px;
    background: var(--lime);
  }
  .brand__name {
    font-family: "Russo One", "Arimo", sans-serif;
    font-size: 40px;
    line-height: 1.02;
    color: var(--lime);
    text-transform: uppercase;
    letter-spacing: 0.5px;
  }
  .brand__tagline {
    margin-top: 6px;
    font-size: 17px;
    color: var(--silver);
    letter-spacing: 0.3px;
  }

  .card--back .brand { top: 108px; left: 60px; }
  .card--back .brand__divider { background: var(--emboss); }
  .card--back .brand__name { color: var(--emboss); }
  .card--back .brand__tagline { color: var(--emboss); }

  .person {
    position: absolute;
    left: 48px;
    top: 232px;
    font-size: 14px;
    line-height: 1.3;
  }
  .person__name { font-size: 22px; color: var(--white); margin-bottom: 4px; }
  .person__credentials { color: var(--lime); }
  .person__title, .person__city { color: var(--blue); }

  .contact {
    position: absolute;
    left: 320px;
    top: 246px;
    list-style: none;
    font-size: 16px;
    color: var(--white);
  }
  .contact__item { display: flex; align-items: center; height: 24px; white-space: nowrap; }
  .contact__icon { width: 14px; height: 14px; margin-right: 10px; flex: none; }
</style>
</head>
<body>

<section class="card card--back" aria-label="Card back">
  <div class="brand">
    <svg class="brand__mark" viewBox="0 0 150 150" aria-hidden="true">
      <circle cx="75" cy="75" r="66" fill="none" stroke="var(--emboss)" stroke-width="6"/>
    </svg>
    <div class="brand__divider"></div>
    <div>
      <div class="brand__name">K7R Motion<br>Dynamics</div>
      <div class="brand__tagline">Strength and Conditioning</div>
    </div>
  </div>
</section>

<section class="card card--front" aria-label="Card front">
  <div class="brand">
    <svg class="brand__mark" viewBox="0 0 150 150" aria-hidden="true">
      <circle cx="75" cy="75" r="66" fill="none" stroke="var(--lime)" stroke-width="6"/>
    </svg>
    <div class="brand__divider"></div>
    <div>
      <div class="brand__name">K7R Motion<br>Dynamics</div>
      <div class="brand__tagline">Strength and Conditioning</div>
    </div>
  </div>

  <div class="person">
    <div class="person__name">Lorenzo Baptiste</div>
    <div class="person__credentials">MA, CPT, NSCP</div>
    <div class="person__title">Head of Athletic Development</div>
    <div class="person__city">Riverbend, ST</div>
  </div>

  <ul class="contact">
    <li class="contact__item">
      <svg class="contact__icon" viewBox="0 0 14 14" aria-hidden="true">
        <path d="M3 1h3l1 3-2 1.5a8 8 0 0 0 3.5 3.5L10 7l3 1v3a2 2 0 0 1-2 2A10 10 0 0 1 1 3a2 2 0 0 1 2-2z" fill="var(--lime)"/>
      </svg>
      (555) 318-7046
    </li>
    <li class="contact__item">
      <svg class="contact__icon" viewBox="0 0 14 14" aria-hidden="true">
        <rect x="1" y="3" width="12" height="8" fill="var(--lime)"/>
        <path d="M1 3l6 5 6-5" fill="none" stroke="var(--card)" stroke-width="1.4"/>
      </svg>
      k7rmotiondynamics@quikmailbox.net
    </li>
    <li class="contact__item">
      <svg class="contact__icon" viewBox="0 0 14 14" aria-hidden="true">
        <rect x="1.5" y="1.5" width="11" height="11" rx="2" fill="none" stroke="var(--lime)" stroke-width="2"/>
      </svg>
      lift_mentor_lb
    </li>
  </ul>
</section>

</body>
</html>
```